Birchway Swing Studio New Location Postcard

I need a postcard announcing our new location. It is a indoor golf training facility that offers award winner instruction, state-of-the-art technology, and custom club fitting. Whether you are a beginner, an aspiring athlete, or an amateur, Birchway Swing Studio offers personalized programs to help take your game to the next level. Call now to schedule your free tour or to sign up. Limited memberships available.
I would like somewhere are on postcard to say Don't put away your clubs just yet! The course may be closed but Birchway Swing Studio's new indoor location is open!
Industry/Entity Type
Training
Look and feel
Each slider illustrates characteristics of the customer's brand and the style your logo design should communicate.

```html
<!DOCTYPE html>
<html lang="en">
<head>
<meta charset="utf-8">
<title>Birchway Swing Studio – New Location Postcard</title>
<link href="https://fonts.googleapis.com/css2?family=Oswald:wght@500;700&family=Roboto+Condensed:wght@400;700&family=Archivo:wght@600&display=swap" rel="stylesheet">
<style>
  :root {
    --backdrop: #e6e4df;
    --charcoal: #333333;
    --grass-light: #a6d24a;
    --grass-mid: #6cbf3c;
    --grass-deep: #22ad4b;
    --brand-red: #e53a35;
    --sun-yellow: #fff200;
    --call-green: #1fa84a;
    --sign-blue: #1ba7e1;
    --white: #ffffff;
    --map-grey: #e9e9e7;
  }
  * { margin: 0; padding: 0; box-sizing: border-box; }
  html, body { width: 799px; height: 1200px; overflow: hidden; }
  body { background: var(--backdrop); position: relative; font-family: "Roboto Condensed", sans-serif; }

  .postcard { position: absolute; left: 82px; width: 636px; height: 490px; overflow: hidden; }
  .postcard--front { top: 86px; }
  .postcard--back { top: 633px; background: linear-gradient(180deg, var(--grass-light) 0%, var(--grass-mid) 45%, var(--grass-deep) 100%); }

  .grass-photo { position: absolute; inset: 0; background: linear-gradient(180deg, #9fcf52 0%, #7dbb3a 45%, #5fa62c 100%); }
  .header-band { position: absolute; left: 0; top: 0; width: 636px; height: 190px; }

  .brand-mark { position: absolute; border-radius: 50%; background: var(--white); display: flex; align-items: center; justify-content: center; text-align: center; }
  .brand-mark__name { font-family: "Oswald", sans-serif; font-weight: 700; color: var(--brand-red); text-transform: uppercase; line-height: 1.05; }
  .postcard--front .brand-mark { left: 22px; top: 49px; width: 122px; height: 122px; }
  .postcard--front .brand-mark__name { font-size: 19px; }
  .postcard--back .brand-mark { left: 33px; top: 25px; width: 126px; height: 126px; }
  .postcard--back .brand-mark__name { font-size: 20px; }

  .announce { position: absolute; left: 168px; top: 36px; width: 450px; }
  .announce__title { font-family: "Oswald", sans-serif; font-weight: 700; font-size: 26px; color: var(--sun-yellow); letter-spacing: 0.2px; line-height: 1.1; }
  .announce__body { margin-top: 6px; color: var(--white); font-size: 18.5px; line-height: 24px; }

  .offer { position: absolute; left: 0; width: 100%; top: 186px; text-align: center; color: var(--charcoal); font-weight: 700; font-size: 23px; line-height: 30px; }

  .cta { position: absolute; left: 0; width: 100%; top: 257px; text-align: center; font-family: "Archivo", sans-serif; font-weight: 600; font-size: 28.5px; line-height: 35px; color: var(--charcoal); text-transform: uppercase; }
  .cta__tag { padding: 0 4px; }
  .cta__tag--call { background: var(--call-green); color: var(--charcoal); }
  .cta__tag--sign { background: var(--sign-blue); color: var(--charcoal); }

  .limited { position: absolute; left: 128px; top: 333px; width: 382px; height: 30px; }
  .limited__bar { position: absolute; inset: 0; background: var(--brand-red); transform: skewX(-10deg); }
  .limited__text { position: relative; display: block; text-align: center; color: var(--white); font-family: "Archivo", sans-serif; font-weight: 600; font-size: 20px; line-height: 30px; }

  .closing { position: absolute; left: 0; width: 100%; top: 375px; text-align: center; font-weight: 700; }
  .closing__hook { color: var(--sun-yellow); font-family: "Oswald", sans-serif; font-weight: 700; font-size: 30px; line-height: 38px; }
  .closing__note { color: var(--charcoal); font-size: 23px; line-height: 26px; }
  .closing__open { color: var(--white); font-size: 28px; line-height: 34px; }

  .back-title { position: absolute; left: 178px; top: 48px; font-family: "Oswald", sans-serif; font-weight: 700; font-size: 40px; line-height: 52px; color: var(--charcoal); text-transform: uppercase; white-space: nowrap; }
  .open-band { position: absolute; left: 0; top: 111px; width: 636px; height: 62px; background: var(--charcoal); }
  .open-band__text { position: absolute; left: 172px; top: 0; font-family: "Oswald", sans-serif; font-weight: 500; font-size: 34px; letter-spacing: -0.3px; line-height: 62px; color: var(--white); text-transform: uppercase; white-space: nowrap; }

  .location-map { position: absolute; left: 136px; top: 179px; width: 380px; height: 238px; border: 5px solid var(--white); background: linear-gradient(135deg, var(--map-grey) 0%, #f2efe6 50%, #dcdcd8 100%); }
  .location-map__pin { position: absolute; left: 176px; top: 95px; width: 20px; height: 30px; }

  .back-hook { position: absolute; left: 0; width: 100%; top: 432px; text-align: center; font-family: "Oswald", sans-serif; font-weight: 700; font-size: 31px; line-height: 40px; color: var(--charcoal); }
</style>
</head>
<body>

<section class="postcard postcard--front">
  <div class="grass-photo" role="img" aria-label="Photo of a sunlit golf course fairway"></div>

  <svg class="header-band" viewBox="0 0 636 190" aria-hidden="true">
    <polygon points="0,0 636,0 636,182 180,182 160,160 0,160" fill="var(--charcoal)"/>
    <polygon points="0,100 0,112 150,170 170,190 636,190 636,182 180,182 160,160 0,104" fill="var(--grass-deep)"/>
  </svg>

  <div class="brand-mark"><span class="brand-mark__name">Birchway<br>Swing<br>Studio</span></div>

  <div class="announce">
    <h1 class="announce__title">ANNOUNCING OUR NEW LOCATION.</h1>
    <p class="announce__body">It is a indoor golf training facility that offers<br>award winner instruction, state-of-the-art technology,<br>and custom club fitting. Whether you are a beginner,<br>an aspiring athlete, or an amateur,</p>
  </div>

  <p class="offer">Birchway Swing Studio offers personalized programs<br>to help take your game to the next level.</p>

  <p class="cta"><span class="cta__tag cta__tag--call">Call now</span> to schedule your<br>free tour or to <span class="cta__tag cta__tag--sign">sign up.</span></p>

  <div class="limited"><span class="limited__bar"></span><span class="limited__text">Limited memberships available.</span></div>

  <div class="closing">
    <p class="closing__hook">Don’t put away your clubs just yet!</p>
    <p class="closing__note">The course may be closed but</p>
    <p class="closing__open">Birchway Swing Studio’s new indoor location is open!</p>
  </div>
</section>

<section class="postcard postcard--back">
  <div class="open-band"><span class="open-band__text">New indoor location is open!</span></div>
  <div class="brand-mark"><span class="brand-mark__name">Birchway<br>Swing<br>Studio</span></div>
  <h2 class="back-title">Birchway Swing Studio’s</h2>

  <div class="location-map" role="img" aria-label="Street map showing the studio's new location">
    <svg class="location-map__pin" viewBox="0 0 20 30" aria-hidden="true">
      <path d="M10 0C4.5 0 0 4.4 0 9.8 0 17 10 30 10 30s10-13 10-20.2C20 4.4 15.5 0 10 0z" fill="var(--brand-red)"/>
      <circle cx="10" cy="10" r="3.5" fill="#8b1a17"/>
    </svg>
  </div>

  <p class="back-hook">Don’t put away your clubs just yet!</p>
</section>

</body>
</html>
```